Business IT Services Billboard to attract local small businesses

We are Brivolane, a premier Managed Service Provider (MSP) specializing in comprehensive IT services and VOIP phone solutions exclusively for businesses. Our goal is to create a dynamic and visually engaging billboard advertisement that not only highlights our cutting-edge IT solutions but also emphasizes our state-of-the-art VOIP phone services. This billboard should communicate our commitment to providing innovative, reliable, and holistic technology solutions.
Target Market(s)
small business
Industry/Entity Type
Information Technology
Colors
Designer to choose colors to be used in the design.
Look and feel
Each slider illustrates characteristics of the customer's brand and the style your logo design should communicate.

```html
<!DOCTYPE html>
<html lang="en">
<head>
<meta charset="utf-8">
<title>Brivolane – IT and VOIP Services Billboard</title>
<link rel="stylesheet" href="https://fonts.googleapis.com/css2?family=Montserrat:wght@600;700;800;900&display=swap">
<style>
  :root {
    --brand-blue: #1877fd;
    --band-blue: #5e9ffb;
    --steel-grey: #adbcbb;
    --page-grey: #b3b3b3;
    --white: #ffffff;
    --ice: #f3fafd;
  }
  html, body {
    margin: 0;
    padding: 0;
    width: 1200px;
    height: 780px;
    overflow: hidden;
    background: var(--page-grey);
    font-family: "Montserrat", Arial, sans-serif;
  }
  .billboard {
    position: absolute;
    left: 0;
    top: 52px;
    width: 1200px;
    height: 675px;
    background: linear-gradient(180deg, var(--white) 0%, var(--white) 55%, var(--ice) 100%);
    overflow: hidden;
  }
  .shapes { position: absolute; inset: 0; }
  .hero-photo {
    position: absolute;
    left: 500px;
    top: 0;
    width: 675px;
    height: 394px;
    background:
      radial-gradient(ellipse at 78% 62%, rgba(196,140,110,0.55) 0%, rgba(196,140,110,0) 38%),
      radial-gradient(ellipse at 60% 10%, rgba(250,220,200,0.6) 0%, rgba(250,220,200,0) 30%),
      linear-gradient(90deg, rgba(255,255,255,0) 0%, #e6f0f8 45%, #d7e6f2 100%);
  }
  .brand-name {
    position: absolute;
    left: 138px;
    top: 88px;
    margin: 0;
    font-size: 52px;
    font-weight: 900;
    color: var(--brand-blue);
    letter-spacing: 1px;
    line-height: 1;
  }
  .headline {
    position: absolute;
    left: 588px;
    top: 70px;
    margin: 0;
    color: var(--white);
    line-height: 1;
  }
  .headline .lead { display: block; font-size: 31px; font-weight: 700; letter-spacing: 0.5px; }
  .headline .name { display: block; font-size: 60px; font-weight: 900; letter-spacing: 2px; margin-top: 6px; }
  .headline .services { display: block; font-size: 43px; font-weight: 700; margin-top: 2px; }
  .tagline {
    position: absolute;
    left: 41px;
    top: 290px;
    margin: 0;
    font-size: 35px;
    font-weight: 700;
    line-height: 44px;
    color: var(--white);
  }
  .subline {
    position: absolute;
    left: 41px;
    top: 484px;
    margin: 0;
    font-size: 26px;
    font-weight: 700;
    line-height: 39px;
    color: var(--brand-blue);
  }
  .cta-lead {
    position: absolute;
    left: 713px;
    top: 560px;
    margin: 0;
    font-size: 21px;
    font-weight: 700;
    color: var(--white);
  }
  .cta-url {
    position: absolute;
    left: 689px;
    top: 608px;
    margin: 0;
    font-size: 41px;
    font-weight: 700;
    color: var(--white);
    letter-spacing: 0.5px;
  }
</style>
</head>
<body>
<main class="billboard">
  <div class="hero-photo" role="img" aria-label="Photo of a hand touching a glowing digital interface with circuit lines and icons"></div>

  <svg class="shapes" width="1200" height="675" viewBox="0 0 1200 675" aria-hidden="true">
    <polygon class="headline-band" points="576,41 1200,41 1200,241 499,241" fill="var(--band-blue)" opacity="0.95"/>
    <polygon class="tagline-band" points="0,259 599,259 545,394 1200,394 1200,414 537,414 527,448 0,448" fill="var(--brand-blue)"/>
    <polygon class="cta-grey-band" points="711,546 1200,546 1200,597 690,597" fill="var(--steel-grey)"/>
    <polygon class="cta-blue-band" points="604,598 1200,598 1200,675 575,675" fill="var(--brand-blue)"/>
  </svg>

  <p class="brand-name">Brivolane</p>

  <h1 class="headline">
    <span class="lead">Elevate Your Business with</span>
    <span class="name">BRIVOLANE</span>
    <span class="services">IT and VOIP Services</span>
  </h1>

  <p class="tagline">SEAMLESS TECHNOLOGY<br>SOLUTIONS FOR<br>MODERN BUSINESSES</p>

  <p class="subline">INNOVATIVE IT AND VOIP SOLUTIONS<br>TAILORED FOR YOUR BUSINESS SUCCESS.</p>

  <p class="cta-lead">TRANSFORM YOUR TECH TODAY AT</p>
  <p class="cta-url">www.brivolane.com</p>
</main>
</body>
</html>
```